Designing a "Yummy Mummy" Style Blog

I am clueless when it comes to technology and web design. I am starting a blog on pregnancy, babies and high society life in London. It's going to be called "Fizzwicks on Marlow", and will aim to be frank, funny and aspire to a certain type of luxury lifestyle.

I would like a well designed, sophisticated looking blog set up for me. I've never had a blog designed for me online before, so i am not entirely sure how it works but ideally i would like the whole "look set up" so i can get the password, add a domain to it and start inputting my text and pictures.

Basically i looked into setting up one myself on pagecraft/scribbleup.example but i realised that with my very basic know how, what i was going to end up with from the "template suggestions" was going to be pretty generic and i really want something unique and special as i am going to try and promote this alongside my writing career.

I would like a relatively non-fussy layout but the "Fizzwicks on Marlow" title i thought could be designed to look like a bit of a logo, with perhaps a cocktail on one end and a dummy/rattle on the other. I want the whole website to look fashionable, stylish and endorse a "yummy mummy lifestyle".

Ideally it would be very easy for me to upload text and pictures to the blog and it would be very visually appealing to look at and easy to read. It will need to have a list of all my blog posts on the side (obviously which are yet to be written, but the capability to have them all in the readers eye-line when they are eventually written!)

I would like to blog to look more like a website than a standard blog. See www.dapperpavement.example or www.vogrenstrand.example for the type of non-standard blog format i like.

Each post is going to be mainly text but then i would like the ability to add photos to each one. I also want the text spread across the page so that it becomes "about the writing"... what i mean is some blogs have lots of little tabs of text you can click on... i want my blog to scroll down so you read it like a story... a bit like www.bumpandbloomdiary.example or www.penvaleposts.example.

Look forward to seeing what you come up with. as an example of my personal style, please see my website www.roseharwick.example which was a clothing brand i designed a few years ago. See that i had an illustration of myself done (in the about section) i like the idea of some little drawings or something unique to make it original. Many thanks for your work in advance.

Please note, i have only made this work "refundable" because i havent done a web design style job post like this before and obviously have no idea whether this is something that would work (have someone design it online for me" BUT i fully intend to buy a design off here and am very serious about doing so so please know that if your design fits what i am looking for i am definitely buying it, this is a genuine committed request!

Many thanks
Updates

Reason: I am extending the deadline as i have just decided to Guarantee the prize money for the project. My email address is rose@roseharwick.example if you would like to email me any ideas/designs for the blog. Please know that i would like the actual blog set up for me on either pagecraft or scribbleup.example site under FIZZWICKS ON MARLOW (my new blog name). Obviously i will be buying the domain name for this but whoever comes up with the best design i will go onto whichever blog site you recommend, add register the FIZZWICKS ON MARLOW BLOG and then you can do all the design for me. Then you will be guaranteed payment on this site. So just know - whoever describes and shows me through logos, fonts and description the best design for my blog will be the one to do it! And i definitely will be choosing someone! Hope my main description give you enough to work out what kind of a style i want. Very modern, femine, fresh fun and clear but not TACKY.. no gaudy colours or pictures.. i want it to look like a glossy magazine column. THANKS x

Target Market(s)

Target market are trendy london girls and new mothers and mothers-to-be. It should appeal to feminine stylish, educated women.

Industry/Entity Type

Clothing

Requirements
Must have
• It must be set up as a blog on an easy to naviagate blog site that i can have easy access to update with my text and pictures using a password and username. It should also be able to have a domain added to it so i can buy www.inkspillsonmarlow.example if i so wish in the future.

INK SPILLS ON MARLOW the title should be designed to look like a logo and be bold and stand out.

The Font needs to be clear yet stylish. I do not want it to be an "all uppercase" font. I am a writer, so i need the ability to use lowercase and uppercase lettering !

Please make it look very clean and clear cut so the reader knows exactly what shes looking at. Some blogs just look too messy, you dont know what you are meant to be reading.

I want the blog to make it clear what the latest blog post is and have that at the top then have all the other blog posts in an archive style list to the left or right of the page. Please make the font clear enough to read but not too huge.

I am sure this goes without saying, but Please note this blog MUST be completely suitable for the UK. I would like it on a UK blog site, or one that is completely worldwide and works for the UK. (ie if this blog is successful i want to make sure i can promote it/advertise on it with uk brands etc)

```html
<!DOCTYPE html>
<html lang="en">
<head>
<meta charset="utf-8">
<title>Fizzwicks on Marlow</title>
<link rel="stylesheet" href="https://fonts.googleapis.com/css2?family=Arimo:wght@400;700&display=swap">
<style>
:root{
  --page-top:#c6c6c8;
  --page-bottom:#f8f6f7;
  --frame:#7fa9ad;
  --heading:#67848f;
  --body-text:#1f1f1f;
  --link:#3f8aa1;
  --meta-link:#6c8591;
  --sidebar-bg:#edf0f5;
  --sidebar-title:#464646;
  --footer-bg:#a5b9bc;
  --nav-text:#3a3a3a;
  --logo-gold:#b58a34;
}
*{box-sizing:border-box;margin:0;padding:0}
html,body{width:829px;height:1200px;overflow:hidden}
body{
  position:relative;
  font-family:"Arimo",Arial,sans-serif;
  color:var(--body-text);
  background:linear-gradient(to bottom,var(--page-top) 0%,#dcdcde 40%,#eeeaec 70%,var(--page-bottom) 100%);
}
.site-nav{
  position:absolute;left:0;top:0;width:829px;height:51px;
  background:linear-gradient(to bottom,#dedede,#cfcfd1);
}
.site-nav ul{list-style:none;position:relative;height:100%}
.site-nav li{position:absolute;top:5px;height:36px;line-height:36px;font-size:15px;letter-spacing:.8px;color:var(--nav-text);text-align:center}
.site-nav .current{left:53px;width:96px;border:1px solid #a8a8a8;border-radius:5px;background:#c8c8ca}
.nav-about{left:186px;width:90px}
.nav-sample{left:330px;width:120px}
.nav-contact{left:508px;width:80px}

.masthead{
  position:absolute;left:35px;top:53px;width:739px;height:167px;
  border:3px solid var(--frame);
  background:linear-gradient(135deg,#bdbdbf 0%,#e4e4e6 30%,#a9a9ac 55%,#dcdcde 80%,#c4c4c6 100%);
  display:flex;align-items:center;justify-content:center;gap:14px;
}
.masthead .art{width:60px;height:80px;border-radius:6px}
.art-glass{background:linear-gradient(to bottom,#c43838,#d9d0c8)}
.art-dummy{background:linear-gradient(to bottom,#e7b743,#5c86b0)}
.logo-name{font-size:44px;font-weight:700;color:var(--logo-gold);letter-spacing:1px;white-space:nowrap}

.content-frame{
  position:absolute;left:37px;top:228px;width:737px;height:990px;
  background:#fff;border:3px solid var(--frame);border-bottom:none;
}
.posts{position:absolute;left:25px;top:18px;width:475px}
.post{margin-bottom:40px}
.post-title{
  display:flex;gap:6px;align-items:flex-start;
  font-size:31px;font-weight:700;letter-spacing:1.2px;line-height:32px;color:var(--heading);
  margin:14px 0 22px;
}
.post-title svg{flex:none;margin-top:3px}
.post p{font-size:14.5px;line-height:17px;letter-spacing:.35px;margin-bottom:12px}
.post p a{color:var(--meta-link);text-decoration:none}
.post-meta{font-size:13px;letter-spacing:.6px;color:var(--meta-link);margin-top:8px}

.sidebar{
  position:absolute;left:511px;top:9px;width:213px;height:901px;
  background:var(--sidebar-bg);padding:20px 16px 0 16px;
}
.search{width:178px;height:21px;border:1px solid #8a8a8a;border-top-width:2px;background:#fff;position:relative}
.search svg{position:absolute;right:3px;top:2px}
.widget{margin-top:36px;padding-left:4px}
.widget h2{font-size:16px;letter-spacing:.5px;color:var(--sidebar-title);margin-bottom:18px}
.widget ul{list-style:none}
.widget li{position:relative;padding-left:19px;font-size:14px;line-height:18px;letter-spacing:.4px;color:#333;margin-bottom:5px}
.widget li::before{
  content:"";position:absolute;left:2px;top:3px;width:11px;height:11px;background:#2c4a50;border-radius:2px;
}
.widget li::after{
  content:"+";position:absolute;left:2px;top:2px;width:11px;height:11px;line-height:11px;text-align:center;font-size:11px;font-weight:700;color:#fff;
}
.widget a{color:var(--link)}
.widget .plain{color:var(--meta-link);text-decoration:none}

.site-footer{
  position:absolute;left:49px;top:1151px;width:712px;height:49px;
  background:var(--footer-bg);text-align:center;font-size:13.5px;letter-spacing:.5px;padding-top:8px;line-height:16px;
}
.site-footer a{color:#3c4f53;text-decoration:none}
.feed-mark{position:absolute;left:6px;top:10px;width:32px;height:32px;border-radius:5px;background:#f08a24}
</style>
</head>
<body>
<nav class="site-nav">
  <ul>
    <li class="current">HOME</li>
    <li class="nav-about">ABOUT ME</li>
    <li class="nav-sample">SAMPLE PAGE</li>
    <li class="nav-contact">CONTACT</li>
  </ul>
</nav>

<header class="masthead">
  <div class="art art-glass" role="img" aria-label="Cocktail glass illustration"></div>
  <div class="logo-name">FIZZWICKS ON MARLOW</div>
  <div class="art art-dummy" role="img" aria-label="Baby dummy illustration"></div>
</header>

<main class="content-frame">
  <section class="posts">
    <article class="post">
      <h1 class="post-title"><svg width="26" height="26" viewBox="0 0 26 26"><ellipse cx="13" cy="10" rx="11" ry="8.5" fill="#8d9498"/><path d="M9 17 L8 25 L14 18Z" fill="#8d9498"/></svg>Hello world!</h1>
      <p>Welcome to Pagecraft. This is your first post. Edit or delete it, then start blogging!</p>
      <div class="post-meta">1 Comment</div>
    </article>

    <article class="post">
      <h1 class="post-title"><svg width="26" height="26" viewBox="0 0 26 26"><ellipse cx="13" cy="10" rx="11" ry="8.5" fill="#8d9498"/><path d="M9 17 L8 25 L14 18Z" fill="#8d9498"/></svg>Lorem ipsum dolor</h1>
      <p>Lorem ipsum dolor sit amet, alia iudico decore ea pro, ut utinam pertinacia temporibus qui. Habeo quaestio gloriatur ne ius. Ne graeco gubergren torquatos sit, qui cu tollit euripidis conceptam. Nisl antiopam petentium cu vix, ex nullam luptatum suavitate nam.An sit nisl errem, sed eu etiam viris debitis. No elitr convenire moderatius quo. Mea molestie definiebas in. Eros solum electram ut mel, te partem iisque gloriatur eam, ei veniam hendrerit repudiandae has. Detracto invenire est cu.An vim minim timeam alterum. Laudem insolens senserit per ne, eum esse legendos ad. Sit et oratio laudem, vis te diceret blandit liberavisse. Pro ut salutandi quaerendum, his no odio nominavi. In nam esse labore, <a href="#">Continue reading →</a></p>
      <div class="post-meta">Leave a comment</div>
    </article>

    <article class="post">
      <h1 class="post-title"><svg width="26" height="26" viewBox="0 0 26 26"><ellipse cx="13" cy="10" rx="11" ry="8.5" fill="#8d9498"/><path d="M9 17 L8 25 L14 18Z" fill="#8d9498"/></svg>How to: Velmoreau’s ethereal half-up hairstyle</h1>
      <p>Simple yet elegant is how one would describe the beauty look at Velmoreau’s spring 2013 show. The make up was barely there and the hair was pinned half-up, accented with gold headpieces, that added to the overall ethereal feel of the show.</p>
      <p>“The hair at Velmoreau is very natural, yet it’s smooth, not frizzy. I didn’t want to create big hair here today, but I still wanted it to feel very modern and rich. The style also fit with the metal hairpieces that Lucien provided,” explained Tomas Reale, Lumaire Creative Consultant.It is a easy DIY hairstyle as it does not require a lot of effort. The simplicity will allow you to wear this kind of hairstyle on any <a href="#">Continue reading →</a></p>
      <div class="post-meta">Leave a comment</div>
    </article>
  </section>

  <aside class="sidebar">
    <div class="search"><svg width="15" height="15" viewBox="0 0 15 15"><circle cx="6" cy="6" r="4.5" fill="none" stroke="#888" stroke-width="1.4"/><path d="M9.3 9.3 L13.5 13.5" stroke="#888" stroke-width="1.6"/></svg></div>

    <section class="widget">
      <h2>Recent Posts</h2>
      <ul>
        <li><a href="#">Hello world!</a></li>
        <li><a href="#">Lorem ipsum dolor</a></li>
        <li><a href="#">How to: Velmoreau’s ethereal half-up hairstyle</a></li>
        <li><a href="#">Baby Lorem ipsum dolor</a></li>
      </ul>
    </section>

    <section class="widget">
      <h2>Recent Comments</h2>
      <ul>
        <li><a class="plain" href="#">Mr Pagecraft</a> on <a href="#">Hello world!</a></li>
        <li>admin on <a href="#">About Me</a></li>
        <li><a class="plain" href="#">Mr Pagecraft</a> on <a href="#">Baby Lorem ipsum dolor</a></li>
      </ul>
    </section>

    <section class="widget">
      <h2>Archives</h2>
      <ul><li><a href="#">November 2012</a></li></ul>
    </section>

    <section class="widget">
      <h2>Categories</h2>
      <ul><li><a href="#">Uncategorized</a></li></ul>
    </section>

    <section class="widget">
      <h2>Meta</h2>
      <ul>
        <li><a href="#">Log in</a></li>
        <li><a href="#">Entries RSS</a></li>
        <li><a href="#">Comments RSS</a></li>
        <li><a class="plain" href="#">pagecraft.example</a></li>
      </ul>
    </section>
  </aside>
</main>

<footer class="site-footer">
  <div class="feed-mark"></div>
  <div><a href="#">Link1</a> | <a href="#">Link2</a> | <a href="#">Link3</a></div>
  <div>Copyright © 2012. All Rights Reserved.</div>
</footer>
</body>
</html>
```